Harbor Ridge Painting Epoxy Flyer

We need a promotional flyer for a new epoxy floor coatings division of our painting company. We do epoxy garage floor coatings and paver sealing. It needs to be based on and very similar to the attached flyer. The garage floor picture needs to look more realistic, and the before and after pavers pictures should look less shiny but still a good contrast. Include attached logo

```html
<!DOCTYPE html>
<html lang="en">
<head>
<meta charset="utf-8">
<title>Harbor Ridge Painting – Epoxy Flyer</title>
<link href="https://fonts.googleapis.com/css2?family=Bebas+Neue&family=Montserrat:ital,wght@0,500;0,600;0,700;0,800;1,400;1,500&display=swap" rel="stylesheet">
<style>
  :root {
    --green: #2e9441;
    --blue: #24418f;
    --ink: #1d1d1f;
    --white: #ffffff;
    --backdrop: #d6d6d6;
    --rule-green: rgba(255,255,255,0.35);
    --rule-blue: rgba(255,255,255,0.3);
  }
  * { box-sizing: border-box; margin: 0; padding: 0; }
  html, body { width: 1200px; height: 2250px; overflow: hidden; }
  body { background: var(--backdrop); position: relative; font-family: 'Montserrat', sans-serif; }

  .flyer {
    position: absolute; left: 50px; top: 347px;
    width: 1100px; height: 1555px;
    background: var(--white);
    box-shadow: 0 10px 30px rgba(0,0,0,0.18);
    overflow: hidden;
  }
  .abs { position: absolute; }
  .display { font-family: 'Bebas Neue', sans-serif; font-weight: 400; text-transform: uppercase; white-space: nowrap; }

  /* Brand */
  .brand { left: 52px; top: 100px; display: flex; align-items: center; gap: 18px; }
  .brand-dot { width: 76px; height: 76px; border-radius: 50%; background: var(--green); flex: none; }
  .brand-name { font-weight: 800; font-size: 31px; line-height: 1.1; color: var(--blue); letter-spacing: 0.5px; }

  /* Headline */
  .headline-top { left: 442px; top: 48px; font-size: 76px; line-height: 1; color: var(--green); letter-spacing: 1px; }
  .headline-main { left: 440px; top: 104px; font-size: 136px; line-height: 1; color: var(--blue); letter-spacing: 1px; }
  .subhead { left: 444px; top: 234px; font-style: italic; font-weight: 400; font-size: 34px; line-height: 1.2; color: var(--ink); white-space: nowrap; }

  /* Gallery */
  .gallery { left: 41px; top: 301px; width: 1018px; height: 436px; }
  .gallery-label { position: absolute; height: 48px; line-height: 52px; text-align: center; font-size: 36px; color: var(--white); }
  .label-floor-before { left: 104px; top: 301px; width: 200px; }
  .label-floor-after { left: 467px; top: 301px; width: 200px; }
  .label-paver-before { left: 836px; top: 465px; width: 180px; }
  .label-paver-after { left: 862px; top: 691px; width: 180px; height: 46px; line-height: 50px; }

  /* Services */
  .services { left: 41px; top: 775px; width: 1018px; height: 287px; }
  .service { position: absolute; color: var(--white); }
  .service-epoxy { left: 96px; top: 804px; width: 370px; }
  .service-paver { left: 563px; top: 804px; width: 440px; }
  .service-title { font-size: 38px; line-height: 1; margin-bottom: 8px; }
  .benefits { list-style: none; }
  .benefits li {
    display: flex; align-items: center; gap: 14px; white-space: nowrap;
    height: 51px; font-style: italic; font-size: 18.5px; font-weight: 400;
  }
  .service-epoxy .benefits li + li { border-top: 1px solid var(--rule-green); }
  .service-paver .benefits li + li { border-top: 1px solid var(--rule-blue); }
  .tick { width: 23px; height: 23px; flex: none; }

  /* Value line */
  .value-line { left: 0; width: 1100px; top: 1092px; text-align: center; font-size: 44px; line-height: 1; color: var(--blue); letter-spacing: 0.5px; }
  .value-line .accent { color: var(--green); }

  /* Trust badges */
  .trust { top: 1148px; left: 0; width: 1100px; height: 90px; }
  .badge { position: absolute; top: 0; display: flex; align-items: center; gap: 14px; }
  .badge-icon { width: 86px; height: 86px; flex: none; }
  .badge-text { font-weight: 600; font-size: 23.5px; line-height: 1.25; color: var(--ink); white-space: nowrap; }
  .badge-licensed { left: 97px; }
  .badge-family { left: 361px; }
  .badge-area { left: 671px; }
  .divider { position: absolute; top: 6px; width: 2px; height: 76px; background: #c9c9c9; }

  /* Call to action */
  .cta-band { left: 0; top: 1264px; width: 1100px; height: 72px; }
  .cta-text { left: 0; width: 980px; top: 1264px; height: 72px; line-height: 78px; text-align: center; font-size: 62px; color: var(--white); }
  .phone { left: 98px; top: 1352px; display: flex; align-items: center; gap: 22px; }
  .phone-icon { width: 66px; height: 88px; }
  .phone-number { font-weight: 800; font-size: 124px; color: var(--ink); letter-spacing: -2px; line-height: 1.05; white-space: nowrap; }
  .promise { left: 0; width: 1100px; top: 1470px; text-align: center; font-style: italic; font-size: 34px; color: var(--ink); }
</style>
</head>
<body>
<main class="flyer">

  <div class="abs brand">
    <span class="brand-dot"></span>
    <span class="brand-name">HARBOR RIDGE<br>PAINTING</span>
  </div>

  <h1>
    <span class="abs display headline-top">Upgrade Your Garage</span>
    <span class="abs display headline-main">&amp; Driveway</span>
  </h1>
  <p class="abs subhead">From worn-out to like new</p>

  <svg class="abs gallery" viewBox="0 0 720 308" preserveAspectRatio="none">
    <defs>
      <linearGradient id="concrete" x1="0" y1="0" x2="1" y2="1">
        <stop offset="0" stop-color="#b7bec3"/><stop offset="0.5" stop-color="#8e989e"/><stop offset="1" stop-color="#737d83"/>
      </linearGradient>
      <linearGradient id="epoxy" x1="0" y1="0" x2="1" y2="1">
        <stop offset="0" stop-color="#8f98a6"/><stop offset="1" stop-color="#a9b0bb"/>
      </linearGradient>
      <linearGradient id="paverOld" x1="0" y1="0" x2="1" y2="1">
        <stop offset="0" stop-color="#a9a29c"/><stop offset="1" stop-color="#8c7a72"/>
      </linearGradient>
      <linearGradient id="paverNew" x1="0" y1="0" x2="1" y2="1">
        <stop offset="0" stop-color="#c0705a"/><stop offset="1" stop-color="#9c4f3e"/>
      </linearGradient>
    </defs>
    <g role="img" aria-label="Worn grey concrete garage floor before coating">
      <polygon points="0,0 227,0 282,308 0,308" fill="url(#concrete)"/>
    </g>
    <g role="img" aria-label="Garage floor finished with speckled epoxy flake coating">
      <polygon points="235,0 500,0 563,308 293,308" fill="url(#epoxy)"/>
    </g>
    <g role="img" aria-label="Faded weathered brick pavers before sealing">
      <polygon points="508,0 720,0 720,150 536,150" fill="url(#paverOld)"/>
    </g>
    <g role="img" aria-label="Brick pavers with restored rich red colour after sealing">
      <polygon points="541,159 720,159 720,308 568,308" fill="url(#paverNew)"/>
    </g>
    <polygon points="0,0 227,0 233,34 0,34" fill="#2e9441"/>
    <polygon points="235,0 500,0 507,34 241,34" fill="#24418f"/>
    <polygon points="530,116 720,116 720,150 536,150" fill="#2e9441"/>
    <polygon points="562,276 720,276 720,308 568,308" fill="#24418f"/>
  </svg>
  <span class="display gallery-label label-floor-before">Before</span>
  <span class="display gallery-label label-floor-after">After</span>
  <span class="display gallery-label label-paver-before">Before</span>
  <span class="display gallery-label label-paver-after">After</span>

  <svg class="abs services" viewBox="0 0 720 203" preserveAspectRatio="none">
    <polygon points="0,0 299,0 341,203 0,203" fill="#2e9441"/>
    <polygon points="309,0 720,0 720,203 351,203" fill="#24418f"/>
  </svg>

  <section class="service service-epoxy">
    <h2 class="display service-title">Epoxy Floor Coatings</h2>
    <ul class="benefits">
      <li><svg class="tick" viewBox="0 0 24 24"><circle cx="12" cy="12" r="11" fill="#fff"/><path d="M7 12.5l3.3 3.2L17 9" fill="none" stroke="#2e9441" stroke-width="2.6" stroke-linecap="round" stroke-linejoin="round"/></svg>Durable, long-lasting finish</li>
      <li><svg class="tick" viewBox="0 0 24 24"><circle cx="12" cy="12" r="11" fill="#fff"/><path d="M7 12.5l3.3 3.2L17 9" fill="none" stroke="#2e9441" stroke-width="2.6" stroke-linecap="round" stroke-linejoin="round"/></svg>Protects from sun fading</li>
      <li><svg class="tick" viewBox="0 0 24 24"><circle cx="12" cy="12" r="11" fill="#fff"/><path d="M7 12.5l3.3 3.2L17 9" fill="none" stroke="#2e9441" stroke-width="2.6" stroke-linecap="round" stroke-linejoin="round"/></svg>Helps prevent weeds &amp; sand loss</li>
      <li><svg class="tick" viewBox="0 0 24 24"><circle cx="12" cy="12" r="11" fill="#fff"/><path d="M7 12.5l3.3 3.2L17 9" fill="none" stroke="#2e9441" stroke-width="2.6" stroke-linecap="round" stroke-linejoin="round"/></svg>Easier to clean &amp; maintain</li>
    </ul>
  </section>

  <section class="service service-paver">
    <h2 class="display service-title">Paver Sealing</h2>
    <ul class="benefits">
      <li><svg class="tick" viewBox="0 0 24 24"><circle cx="12" cy="12" r="11" fill="#fff"/><path d="M7 12.5l3.3 3.2L17 9" fill="none" stroke="#24418f" stroke-width="2.6" stroke-linecap="round" stroke-linejoin="round"/></svg>Restores color &amp; enhances appearance</li>
      <li><svg class="tick" viewBox="0 0 24 24"><circle cx="12" cy="12" r="11" fill="#fff"/><path d="M7 12.5l3.3 3.2L17 9" fill="none" stroke="#24418f" stroke-width="2.6" stroke-linecap="round" stroke-linejoin="round"/></svg>Protects from sun fading</li>
      <li><svg class="tick" viewBox="0 0 24 24"><circle cx="12" cy="12" r="11" fill="#fff"/><path d="M7 12.5l3.3 3.2L17 9" fill="none" stroke="#24418f" stroke-width="2.6" stroke-linecap="round" stroke-linejoin="round"/></svg>Helps prevent weeds &amp; sand loss</li>
      <li><svg class="tick" viewBox="0 0 24 24"><circle cx="12" cy="12" r="11" fill="#fff"/><path d="M7 12.5l3.3 3.2L17 9" fill="none" stroke="#24418f" stroke-width="2.6" stroke-linecap="round" stroke-linejoin="round"/></svg>Easier to clean &amp; maintain</li>
    </ul>
  </section>

  <p class="abs display value-line">Practical upgrades that protect and <span class="accent">improve your home</span></p>

  <div class="abs trust">
    <div class="badge badge-licensed">
      <svg class="badge-icon" viewBox="0 0 86 86">
        <circle cx="43" cy="43" r="39" fill="none" stroke="#2e9441" stroke-width="4"/>
        <path d="M40 20l17 6v13c0 12-8 20-17 24-9-4-17-12-17-24V26z" fill="#24418f"/>
        <circle cx="50" cy="52" r="11" fill="#fff" stroke="#24418f" stroke-width="3"/>
        <path d="M45 52l3.5 3.5L55 48.5" fill="none" stroke="#24418f" stroke-width="3" stroke-linecap="round" stroke-linejoin="round"/>
      </svg>
      <span class="badge-text">Licensed &amp;<br>Insured</span>
    </div>
    <span class="divider" style="left:345px"></span>
    <div class="badge badge-family">
      <svg class="badge-icon" viewBox="0 0 86 86">
        <circle cx="43" cy="43" r="39" fill="none" stroke="#2e9441" stroke-width="4"/>
        <path d="M32 22l2 4.5 4.8.4-3.7 3.2 1.1 4.7L32 32.3l-4.2 2.5 1.1-4.7-3.7-3.2 4.8-.4z" fill="#24418f"/>
        <path d="M43 17l2.3 5 5.4.5-4.1 3.6 1.2 5.3L43 28.6l-4.8 2.8 1.2-5.3-4.1-3.6 5.4-.5z" fill="#24418f"/>
        <path d="M54 22l2 4.5 4.8.4-3.7 3.2 1.1 4.7L54 32.3l-4.2 2.5 1.1-4.7-3.7-3.2 4.8-.4z" fill="#24418f"/>
        <path d="M18 50h8l10 4h10a3 3 0 010 6H36M26 62l14 4 26-10a3 3 0 00-3-5l-13 4" fill="none" stroke="#24418f" stroke-width="3.5" stroke-linecap="round" stroke-linejoin="round"/>
      </svg>
      <span class="badge-text">Family-Owned<br>Local Business</span>
    </div>
    <span class="divider" style="left:653px"></span>
    <div class="badge badge-area">
      <svg class="badge-icon" viewBox="0 0 86 86">
        <circle cx="43" cy="43" r="39" fill="none" stroke="#2e9441" stroke-width="4"/>
        <path d="M43 68C34 56 28 47 28 38a15 15 0 0130 0c0 9-6 18-15 30z" fill="#24418f"/>
        <circle cx="43" cy="38" r="7" fill="#fff"/>
      </svg>
      <span class="badge-text">Serving Prescott &amp;<br>Surrounding Areas</span>
    </div>
  </div>

  <svg class="abs cta-band" viewBox="0 0 778 51" preserveAspectRatio="none">
    <polygon points="0,0 682,0 692,51 0,51" fill="#24418f"/>
    <polygon points="692,0 778,0 778,51 702,51" fill="#2e9441"/>
  </svg>
  <p class="abs display cta-text">Call for a free estimate</p>

  <div class="abs phone">
    <svg class="phone-icon" viewBox="0 0 48 64">
      <path d="M10 4c3-2 6-1 7 2l4 10c1 3 0 5-2 7l-3 2c2 7 6 14 12 19l3-2c2-2 5-2 7 0l7 8c2 2 2 5-1 7l-5 4C31 66 2 36 4 12c0-3 3-6 6-8z" fill="#2e9441"/>
    </svg>
    <span class="phone-number">928-555-0147</span>
  </div>
  <p class="abs promise">Fast, professional service you can trust</p>

</main>
</body>
</html>
```